Website design for Keystone Stewardship Australia, a new boutique specialist consultancy company

We need a web design for a new company based in Australia called Keystone Stewardship Australia (this is abbreviated in our logo to KSA).

KSA is a boutique specialist advisory firm that provides Interim Management and Executive Transition Services. Through a suite of best practice methodologies coupled with advisory and consulting services, KSA supports businesses and executives during times of leadership hiatus and transition which not only mitigates risk of transition failure, but more importantly accelerates transition success.

Delphine at PixelHarbor has designed our logo (see attached file) and the logo and its colours will guide the website design. The primary colour scheme will be in the turquoise/aqua range and may include accent colours - designer's creative choice and guidance is welcome here.

The website should convey an image of crisp, modern professionalism. It's purpose will be to provide information about the company, our products and services and provide contact details. There is no online ordering or payment functionality required. Pages will include a home page with general information about the company, a number of content pages outlining information about each aspect of the services offered, an "about us" page and a "contact us" page.

Target Market(s)

This is a Busines-to-Business company and our target market is primarily large and medium sized companies. The specific individuals targeted at these companies will include:

Human Resources Directors
Talent and Recruitment Heads
Boards and Senior Executive teams of companies
Hiring managers responsible for recruiting and managing senior leaders and executives

Industry/Entity Type

Boutique

Requirements
Should not have
• Online ordering / payment page

```html
<!DOCTYPE html>
<html lang="en">
<head>
<meta charset="utf-8">
<title>Keystone Stewardship Australia</title>
<link href="https://fonts.googleapis.com/css2?family=Open+Sans:ital,wght@0,400;0,600;0,700;1,400&family=Roboto+Condensed:wght@700&display=swap" rel="stylesheet">
<style>
:root{
  --teal:#45b4b4;
  --teal-dark:#2e9697;
  --teal-text:#3aaab0;
  --orange:#e5552a;
  --ink:#333;
  --grey:#777;
  --footer:#333;
  --icon-fill:rgba(255,255,255,.28);
}
*{margin:0;padding:0;box-sizing:border-box}
html,body{width:768px;height:1200px;overflow:hidden;background:#fff}
body{position:relative;font-family:"Open Sans",sans-serif;color:var(--ink)}
.abs{position:absolute}
.head-font{font-family:"Roboto Condensed",sans-serif;font-weight:700;text-transform:uppercase}

/* header */
.brand{left:30px;top:26px;display:flex;align-items:center;gap:8px}
.brand-mark{width:12px;height:12px;background:var(--teal)}
.brand-name{font-weight:600;font-size:15px;color:var(--teal);line-height:1}
.phone{right:45px;top:33px;display:flex;align-items:center;gap:6px;font-size:8.5px;color:var(--orange)}

/* nav */
.nav{left:0;top:64px;width:768px;height:25px;background:linear-gradient(#4fbcbc,var(--teal-dark));border-bottom:1px solid #2a8a8b}
.nav a{position:absolute;top:0;height:25px;line-height:25px;font-size:7px;font-weight:700;color:#fff;text-decoration:none;text-align:center;border-right:1px solid rgba(255,255,255,.25)}
.nav a.active{background:var(--orange)}
.search{left:587px;top:69px;width:144px;height:15px;background:#cdeeee;border:1px solid #a8dede}

/* hero */
.hero{left:0;top:89px;width:768px;height:258px;background:radial-gradient(ellipse at 55% 40%,#f7f7f7,#d9d9d9)}
.hero-photo{left:495px;top:92px;width:165px;height:255px;background:linear-gradient(#d6dce4,#9fb0c4 60%,#3a4150);border-radius:60px 60px 0 0}
.arrow{width:24px;height:24px;border-radius:50%;background:#e9e9e9;border:1px solid #d0d0d0;display:flex;align-items:center;justify-content:center}
.hero-title{left:88px;top:156px;font-size:35px;color:var(--ink);line-height:1}
.hero-sub{left:88px;top:192px;font-size:18px;color:var(--ink);line-height:1}
.hero-text{left:88px;top:220px;width:400px;font-size:10.3px;line-height:12.5px;color:#666}
.btn-orange{left:88px;top:257px;width:84px;height:24px;background:var(--orange);color:#fff;font-size:8px;font-weight:700;text-align:center;line-height:24px;border-radius:2px}

/* service intros */
.intro-photo{width:136px;height:91px}
.intro h2{font-size:15px;color:var(--ink);line-height:1;margin-bottom:8px}
.intro p{font-size:8.2px;line-height:13.6px;color:#666;width:190px}
.intro .more{display:block;margin-top:4px;font-size:7px;color:var(--orange)}

/* supports */
.supports{left:0;top:512px;width:768px;height:301px;background:var(--teal)}
.supports-title{left:0;top:530px;width:768px;text-align:center;font-size:18px;color:#fff}
.supports-lead{left:134px;top:557px;width:500px;text-align:center;font-size:8.3px;line-height:10.5px;font-weight:700;color:#fff;text-transform:uppercase}
.supports-rule{left:214px;top:593px;width:340px;height:8px;border-radius:50%;background:radial-gradient(ellipse,rgba(0,0,0,.22),transparent 70%)}
.support-col{top:625px;width:210px;text-align:center;color:#fff}
.support-col h3{font-size:14px;line-height:1;margin-bottom:14px}
.support-icon{display:block;margin:0 auto 18px;width:56px;height:56px;border-radius:50%;background:var(--icon-fill)}
.support-col p{font-size:8.1px;line-height:11px;width:196px;margin:0 auto}
.btn-white{display:inline-block;margin-top:11px;width:49px;height:24px;line-height:24px;background:#fff;color:var(--teal-text);font-size:8px;font-weight:700;border-radius:3px}

/* news and testimonials */
.section-title{top:851px;font-size:18px;color:var(--ink);line-height:1}
.news-item{left:30px;width:270px;display:flex;gap:6px}
.news-photo{width:52px;height:43px;flex:none}
.news-text{width:210px}
.news-date{font-size:7px;font-style:italic;color:#aaa;line-height:9px}
.news-head{font-size:7.8px;font-weight:600;color:var(--teal-text);line-height:12px;white-space:nowrap}
.news-body{font-size:7px;color:#777;line-height:9.5px}
.news-body span{color:var(--orange)}
.quote{left:382px;width:340px;display:flex;gap:11px}
.avatar{width:44px;height:44px;border-radius:50%;flex:none;background:radial-gradient(circle at 50% 40%,#c9a58a,#5a4a40)}
.quote p{font-size:7.5px;font-style:italic;color:#888;line-height:10.3px;padding-top:3px}
.quote .name{display:block;color:var(--teal-text);margin-top:2px}

/* footer */
.footer{left:0;top:1080px;width:768px;height:120px;background:var(--footer)}
.footer-nav a{position:absolute;top:1102px;font-size:7px;color:#fff;text-decoration:none}
.copyright{left:0;top:1131px;width:768px;text-align:center;font-size:7px;color:#ccc}
.social{left:275px;top:1154px;display:flex;gap:4px}
.social span{width:22px;height:22px;border-radius:50%;background:#6b6b6b}
</style>
</head>
<body>

<header>
  <div class="abs brand"><span class="brand-mark"></span><span class="brand-name">Keystone Stewardship Australia</span></div>
  <div class="abs phone">
    <svg width="18" height="16" viewBox="0 0 18 16"><path d="M4 2c-2 1-2 4 0 7s5 5 7 5l2-2-3-2-1 1c-1 0-3-2-3-3l1-1-2-3z" fill="#e5552a"/><path d="M11 2a5 5 0 0 1 5 5M11 5a2 2 0 0 1 2 2" stroke="#e5552a" fill="none" stroke-width="1.2"/></svg>
    <span>(02) 8123 4567</span>
  </div>
</header>

<nav class="abs nav">
  <a class="active" style="left:30px;width:54px">HOME</a>
  <a style="left:84px;width:68px">ABOUT US</a>
  <a style="left:152px;width:65px">SERVICES</a>
  <a style="left:217px;width:66px">SUPPORT</a>
  <a style="left:283px;width:56px">NEWS</a>
  <a style="left:339px;width:83px">TESTIMONIALS</a>
  <a style="left:422px;width:64px">CONTACT</a>
</nav>
<div class="abs search">
  <svg class="abs" style="right:3px;top:2px" width="10" height="10" viewBox="0 0 10 10"><circle cx="4" cy="4" r="3" stroke="#333" stroke-width="1.4" fill="none"/><path d="M6 6l3 3" stroke="#333" stroke-width="1.6"/></svg>
</div>

<section>
  <div class="abs hero"></div>
  <div class="abs hero-photo" role="img" aria-label="Smiling businessman in shirt and tie with arms crossed"></div>
  <div class="abs arrow" style="left:28px;top:186px"><svg width="10" height="10" viewBox="0 0 10 10"><path d="M7 1L3 5l4 4" stroke="#888" stroke-width="2" fill="none"/></svg></div>
  <div class="abs arrow" style="left:719px;top:186px"><svg width="10" height="10" viewBox="0 0 10 10"><path d="M3 1l4 4-4 4" stroke="#888" stroke-width="2" fill="none"/></svg></div>
  <h1 class="abs head-font hero-title">You `ll be satisfied</h1>
  <div class="abs head-font hero-sub">By the high quality of our services</div>
  <p class="abs hero-text">Lorem ipsum dolor sit amet, consectetur adipisicing elit, sed do eiusmod tempor incididunt ut labore et dolore magna aliqua enim ad minim veniam.</p>
  <div class="abs btn-orange">KNOW MORE</div>
</section>

<section>
  <div class="abs intro-photo" style="left:30px;top:372px;background:linear-gradient(120deg,#2a3a5a,#8a9ab8 55%,#e8ecf2)" role="img" aria-label="Business handshake in front of a chart"></div>
  <div class="abs intro" style="left:182px;top:373px">
    <h2 class="head-font">Interim Management</h2>
    <p>Lorem ipsum dolor sit amet, consectetur adipisicing elit, sed do eiusmod tempor incididunt ut labore et dolore magna aliqua. Ut enim ad minim veniam, quis nostrud</p>
    <span class="more">Read More</span>
  </div>
  <div class="abs intro-photo" style="left:398px;top:372px;background:linear-gradient(#6a7684,#2e3540)" role="img" aria-label="Team of business professionals standing together"></div>
  <div class="abs intro" style="left:550px;top:373px">
    <h2 class="head-font">Executive Transition</h2>
    <p>Lorem ipsum dolor sit amet, consectetur adipisicing elit, sed do eiusmod tempor incididunt ut labore et dolore magna aliqua. Ut enim ad minim veniam, quis nostrud</p>
    <span class="more">Read More</span>
  </div>
</section>

<section>
  <div class="abs supports"></div>
  <h2 class="abs head-font supports-title">Supports</h2>
  <p class="abs supports-lead">Lorem ipsum dolor sit amet, consectetur adipisicing elit, sed do eiusmod tempor incididunt ut labore et dolore magna aliqua. Ut enim ad minim veniam, quis nostrud exercitation ullamco laboris nisi .</p>
  <div class="abs supports-rule"></div>

  <div class="abs support-col" style="left:32px">
    <h3 class="head-font">Business</h3>
    <div class="support-icon" role="img" aria-label="Pictogram of a business person with a briefcase"></div>
    <p>Lorem ipsum dolor sit amet, consectetur adipisicing elit, sed do eiusmod tempor incididunt ut labore et dolore magna aliqua.</p>
    <span class="btn-white">MORE</span>
  </div>
  <div class="abs support-col" style="left:273px">
    <h3 class="head-font">Executives</h3>
    <div class="support-icon" role="img" aria-label="Pictogram of an executive in a suit"></div>
    <p>Lorem ipsum dolor sit amet, consectetur adipisicing elit, sed do eiusmod tempor incididunt ut labore et dolore magna aliqua.</p>
    <span class="btn-white">MORE</span>
  </div>
  <div class="abs support-col" style="left:508px">
    <h3 class="head-font">Management</h3>
    <div class="support-icon" role="img" aria-label="Pictogram of a manager connected to a team"></div>
    <p>Lorem ipsum dolor sit amet, consectetur adipisicing elit, sed do eiusmod tempor incididunt ut labore et dolore magna aliqua.</p>
    <span class="btn-white">MORE</span>
  </div>
</section>

<section>
  <h2 class="abs head-font section-title" style="left:29px">Latest News</h2>
  <article class="abs news-item" style="top:891px">
    <div class="news-photo" style="background:linear-gradient(#dfe3e8,#3a3f48)" role="img" aria-label="Businessman portrait"></div>
    <div class="news-text"><div class="news-date">24, Feb 2014</div><div class="news-head">Lorem ipsum dolor sit amet Consectetur adipisicing elit</div><div class="news-body">Rosed do eiusmod tempor incididunt ut labore et dolore magnaRosed do eiusmod tempor incididunt <span>More</span></div></div>
  </article>
  <article class="abs news-item" style="top:948px">
    <div class="news-photo" style="background:linear-gradient(#eef2f6,#3b78b8)" role="img" aria-label="Smiling businesswoman portrait"></div>
    <div class="news-text"><div class="news-date">24, Feb 2014</div><div class="news-head">Lorem ipsum dolor sit amet Consectetur adipisicing elit</div><div class="news-body">Rosed do eiusmod tempor incididunt ut labore et dolore magnaRosed do eiusmod tempor incididunt <span>More</span></div></div>
  </article>
  <article class="abs news-item" style="top:1005px">
    <div class="news-photo" style="background:linear-gradient(#cfe0ee,#2d3440)" role="img" aria-label="Businessman in suit portrait"></div>
    <div class="news-text"><div class="news-date">24, Feb 2014</div><div class="news-head">Lorem ipsum dolor sit amet Consectetur adipisicing elit</div><div class="news-body">Rosed do eiusmod tempor incididunt ut labore et dolore magnaRosed do eiusmod tempor incididunt <span>More</span></div></div>
  </article>

  <h2 class="abs head-font section-title" style="left:388px">Testimonials</h2>
  <blockquote class="abs quote" style="top:892px">
    <div class="avatar" role="img" aria-label="Client portrait"></div>
    <p>Rosed do eiusmod tempor incididunt ut labore et dolore magnaRosed do eiusmod tempor incididuntRosed do eiusmod tempor incididunt ut labore et dolore magnaRosed do eiusmod tempor incididunt<span class="name">- Marcus Hale</span></p>
  </blockquote>
  <blockquote class="abs quote" style="top:949px">
    <div class="avatar" role="img" aria-label="Client portrait"></div>
    <p>Rosed do eiusmod tempor incididunt ut labore et dolore magnaRosed do eiusmod tempor incididuntRosed do eiusmod tempor incididunt ut labore et dolore magnaRosed do eiusmod tempor incididunt<span class="name">- Marcus Hale</span></p>
  </blockquote>
  <blockquote class="abs quote" style="top:1006px">
    <div class="avatar" role="img" aria-label="Client portrait"></div>
    <p>Rosed do eiusmod tempor incididunt ut labore et dolore magnaRosed do eiusmod tempor incididuntRosed do eiusmod tempor incididunt ut labore et dolore magnaRosed do eiusmod tempor incididunt<span class="name">- Marcus Hale</span></p>
  </blockquote>
</section>

<footer>
  <div class="abs footer"></div>
  <nav class="footer-nav">
    <a style="left:172px">ABOUT US</a>
    <a style="left:240px">SERVICES</a>
    <a style="left:304px">SUPPORT</a>
    <a style="left:369px">NEWS</a>
    <a style="left:423px">TESTIMONIALS</a>
    <a style="left:505px">CONTACT</a>
  </nav>
  <div class="abs copyright">ALL RIGHTS RESERVED. COPYRIGHTS @ 2014</div>
  <div class="abs social" aria-label="Social links"><span></span><span></span><span></span><span></span><span></span><span></span><span></span></div>
</footer>

</body>
</html>
```